Stationery Design Project for import company - Kelvo Trading

We are a import company that sells branded products to large retailers in New Zealand.
We need a simple, professional looking Logo, Business Cards, Email Signature and Letterhead.
Design needs to have some colour in it but nothing too bright or youthful.
The brand is business to business.
The companies name is Kelvo Trading.
I have uploaded some examples of business cards that I like
Also need a powerpoint template
The range of products is diverse so the deign needs to be generic. Please note that the business does not sell to consumers only other businesses
Target Market(s)
Buyers at Retail Companies Head Offices (business to business)
Industry/Entity Type
Business
Look and feel
Each slider illustrates characteristics of the customer's brand and the style your logo design should communicate.

```html
<!DOCTYPE html>
<html lang="en">
<head>
<meta charset="utf-8">
<title>Kelvo Trading – Business Card</title>
<link rel="stylesheet" href="https://fonts.googleapis.com/css2?family=Montserrat:wght@400;500;700&display=swap">
<style>
  :root {
    --backdrop: #d6d7d9;
    --card-white: #ffffff;
    --brand-blue: #1f3f8c;
    --ink: #111111;
    --navy-light: #24478f;
    --navy-dark: #0d1f4d;
    --mark-faint: #8a9cc4;
    --divider: #2a4a96;
  }
  * { margin: 0; padding: 0; box-sizing: border-box; }
  html, body {
    width: 1200px; height: 1200px; overflow: hidden;
    background: var(--backdrop);
    font-family: "Montserrat", sans-serif;
  }
  .sheet {
    width: 1200px; height: 1200px;
    display: flex; flex-direction: column;
    align-items: center; justify-content: center; gap: 60px;
  }
  .card {
    width: 900px; height: 514px;
    position: relative;
    box-shadow: 0 6px 18px rgba(0,0,0,0.18);
  }
  /* Front */
  .card-front {
    background: linear-gradient(135deg, #f2f2f2 0%, var(--card-white) 45%, #fafafa 100%);
    display: flex; align-items: center;
  }
  .brand-block {
    width: 430px;
    display: flex; align-items: center; justify-content: center; gap: 16px;
  }
  .brand-square {
    width: 34px; height: 34px; background: var(--brand-blue);
  }
  .brand-name {
    font-weight: 700; font-size: 34px; letter-spacing: 1px;
    color: var(--brand-blue); text-transform: uppercase;
  }
  .divider {
    width: 2px; height: 170px; background: var(--divider);
  }
  .contact-block { padding-left: 40px; }
  .person-name {
    font-weight: 700; font-size: 36px; color: var(--brand-blue);
    letter-spacing: 0.5px; line-height: 1;
  }
  .person-role {
    font-weight: 700; font-size: 15px; color: var(--ink);
    text-align: right; margin-top: 2px; margin-bottom: 22px;
  }
  .contact-list { list-style: none; }
  .contact-list li {
    display: flex; align-items: center; gap: 12px;
    font-size: 16px; font-weight: 500; color: var(--ink);
    line-height: 26px;
  }
  .contact-list svg { width: 16px; height: 16px; flex: none; }
  /* Back */
  .card-back {
    background: radial-gradient(ellipse at 35% 30%, var(--navy-light) 0%, #183777 50%, var(--navy-dark) 100%);
    display: flex; align-items: center; justify-content: center; gap: 26px;
  }
  .back-square {
    width: 64px; height: 64px; background: var(--mark-faint);
  }
  .back-name {
    font-weight: 700; font-size: 66px; letter-spacing: 2px;
    color: var(--mark-faint); text-transform: uppercase;
  }
</style>
</head>
<body>
<main class="sheet">
  <section class="card card-front" aria-label="Business card front">
    <div class="brand-block">
      <span class="brand-square"></span>
      <span class="brand-name">Kelvo Trading</span>
    </div>
    <div class="divider"></div>
    <div class="contact-block">
      <p class="person-name">YOUR NAME.....</p>
      <p class="person-role">POSITION</p>
      <ul class="contact-list">
        <li>
          <svg viewBox="0 0 16 16" aria-hidden="true"><path d="M3 2h3l1.5 3.5-2 1.2a8 8 0 0 0 3.8 3.8l1.2-2L14 10v3a1 1 0 0 1-1 1A11 11 0 0 1 2 3a1 1 0 0 1 1-1z" fill="#111"/></svg>
          00 0000 0000
        </li>
        <li>
          <svg viewBox="0 0 16 16" aria-hidden="true"><rect x="1" y="3" width="14" height="10" fill="#111"/><path d="M1.5 3.5 8 9l6.5-5.5" stroke="#fff" stroke-width="1.4" fill="none"/></svg>
          INFO@KELVOTRADING.COM
        </li>
        <li>
          <svg viewBox="0 0 16 16" aria-hidden="true"><circle cx="8" cy="8" r="6.5" stroke="#111" stroke-width="1.6" fill="none"/><path d="M1.5 8h13M8 1.5c-3 3.5-3 9.5 0 13M8 1.5c3 3.5 3 9.5 0 13" stroke="#111" stroke-width="1.2" fill="none"/></svg>
          WWW.KELVOTRADING.COM
        </li>
      </ul>
    </div>
  </section>

  <section class="card card-back" aria-label="Business card back">
    <span class="back-square"></span>
    <span class="back-name">Kelvo Trading</span>
  </section>
</main>
</body>
</html>
```